" Ponte Dourada é uma loja de artigos religiosos católicos em fase instalação em Brasília - DF, dedicada a oferecer produtos que fortalecem a espiritualidade dos fiéis. A proposta é comercializar terços, imagens sacras, livros, bíblias e artigos litúrgicos em loja física e futuramente online. O diferencial são os produtos personalizados e a implantação de um espaço devocional. A empresa visa tornar-se referência no segmento em nível regional, nacional e online. "

```html
<!DOCTYPE html>
<html lang="pt-BR">
<head>
<meta charset="utf-8">
<title>Ponte Dourada — Fachada</title>
<link rel="stylesheet" href="https://fonts.googleapis.com/css2?family=Cinzel:wght@500;600&family=Montserrat:wght@500&display=swap">
<style>
  :root {
    --bg: #eceef1;
    --navy: #1e2b4d;
    --navy-deep: #17223f;
    --gold: #d8b766;
    --gold-light: #e9d39c;
    --cream: #f3ead2;
  }
  * { margin: 0; padding: 0; box-sizing: border-box; }
  html, body { width: 1200px; height: 1200px; overflow: hidden; background: var(--bg); }
  body { position: relative; font-family: 'Cinzel', serif; }

  .store-sign {
    position: absolute; left: 60px; top: 220px; width: 1080px; height: 300px;
    background: linear-gradient(180deg, var(--navy) 0%, var(--navy-deep) 100%);
    border-bottom: 12px solid var(--gold);
    display: flex; align-items: center; justify-content: center; gap: 48px;
  }
  .store-sign .mark {
    width: 120px; height: 120px; border-radius: 50%; background: var(--gold);
  }
  .store-sign .wordmark { text-align: center; }
  .store-sign .name {
    font-family: 'Cinzel', serif; font-weight: 500; font-size: 84px;
    letter-spacing: 3px; color: var(--cream); line-height: 1;
  }
  .store-sign .tagline {
    margin-top: 22px; font-family: 'Cinzel', serif; font-weight: 500;
    font-size: 30px; letter-spacing: 10px; color: var(--gold-light);
  }

  .door-band {
    position: absolute; left: 60px; top: 720px; width: 1080px; height: 96px;
    background: var(--navy);
    border-top: 4px solid var(--gold); border-bottom: 4px solid var(--gold);
    display: grid; grid-template-columns: repeat(4, 1fr);
  }
  .door-band .cell {
    display: flex; align-items: center; justify-content: center; gap: 14px;
    color: var(--cream); border-right: 3px solid var(--gold);
  }
  .door-band .cell:last-child { border-right: none; }
  .door-band .handle, .door-band .phone {
    font-family: 'Montserrat', sans-serif; font-weight: 500; font-size: 22px; letter-spacing: 0.5px;
  }
  .door-band .dot { width: 26px; height: 26px; border-radius: 50%; background: var(--gold); flex: none; }
  .door-band .mini-name {
    font-family: 'Cinzel', serif; font-weight: 500; font-size: 24px; letter-spacing: 1.5px;
  }
  .door-band svg { flex: none; }
</style>
</head>
<body>
  <header class="store-sign">
    <div class="mark" aria-hidden="true"></div>
    <div class="wordmark">
      <h1 class="name">PONTE DOURADA</h1>
      <p class="tagline">· ARTIGOS RELIGIOSOS ·</p>
    </div>
  </header>

  <section class="door-band">
    <div class="cell">
      <span class="dot" aria-hidden="true"></span>
      <span class="handle">pontedourada</span>
    </div>
    <div class="cell">
      <span class="dot" aria-hidden="true"></span>
      <span class="mini-name">PONTE DOURADA</span>
    </div>
    <div class="cell">
      <svg width="24" height="24" viewBox="0 0 24 24" aria-hidden="true">
        <path d="M6.6 10.8a15.2 15.2 0 0 0 6.6 6.6l2.2-2.2a1 1 0 0 1 1-.25 11.4 11.4 0 0 0 3.6.6 1 1 0 0 1 1 1V20a1 1 0 0 1-1 1A17 17 0 0 1 3 4a1 1 0 0 1 1-1h3.5a1 1 0 0 1 1 1c0 1.25.2 2.45.6 3.6a1 1 0 0 1-.25 1z" fill="#d8b766"/>
      </svg>
      <span class="phone">(61) 9 5555-0142</span>
    </div>
    <div class="cell">
      <span class="dot" aria-hidden="true"></span>
      <span class="mini-name">PONTE DOURADA</span>
    </div>
  </section>
</body>
</html>
```